Business Card Design

We need a business card designed to portray the message that we are wedding and event stylists. We set up garden ceremonies and style wedding reception venues with chair covers and sashes, backdrops and draping's, wishing wells, tealight holders, table centerpieces. We also style corporate functions - Christmas parties, gala dinners, school formals, award nights. The colour of our uniforms are black and hot pink, if these colours could be incorporated. We would like to be able to use this design for letterhead, flyers and postcards etc. We would like the design to portray a professional, classic image that would relate to both spectrums of our business, weddings and corporate events. If you could develop a logo to incorporate would be great

Target Market(s)

brides, corporate compaines

Industry/Entity Type

Wedding

Contact Information for Business Card

Velvet Aisle & Function Rentals
Phone: 0413 586 190 Email:vaafr@quokkamail.com
Web: www.velvetaisleandfunctions.com.au

Requirements
Must have
• Must include that we set up for weddings, engagements, birthdays, anniversaries, corporate functions, school formals, any occasion.

```html
<!DOCTYPE html>
<html lang="en">
<head>
<meta charset="utf-8">
<title>Velvet Aisle &amp; Function Rentals – Card</title>
<link rel="stylesheet" href="https://fonts.googleapis.com/css2?family=Tinos&display=swap">
<style>
  :root {
    --ink: #111111;
    --white: #ffffff;
    --hot-pink: #ff4fa3;
    --panel-top: #f9f9f9;
    --panel-bottom: #858585;
    --rose-top: #fcb8c8;
    --rose-bottom: #a24a68;
    --feature-tint-top: #f7a9c2;
    --feature-tint-bottom: #b35a7c;
  }
  * { margin: 0; padding: 0; box-sizing: border-box; }
  html, body { width: 1200px; height: 686px; overflow: hidden; background: #ffffff; }
  body { font-family: "Tinos", "Times New Roman", serif; color: var(--ink); }

  .card { position: relative; width: 1200px; height: 686px; overflow: hidden; }

  .info-panel {
    position: absolute; left: 0; top: 0; width: 425px; height: 686px;
    background: linear-gradient(to bottom, var(--panel-top), var(--panel-bottom));
  }
  .brand-name { position: absolute; left: 8px; top: 14px; font-size: 29px; font-weight: 400; line-height: 1; white-space: nowrap; color: var(--ink); }
  .brand-sub { position: absolute; left: 232px; top: 48px; font-size: 23px; line-height: 1; }
  .brand-rule { position: absolute; left: 14px; top: 85px; width: 394px; height: 2px; background: var(--hot-pink); }

  .about-title { position: absolute; left: 0; width: 412px; top: 134px; text-align: center; font-size: 34px; font-weight: 400; }
  .about-text { position: absolute; left: 14px; top: 203px; width: 400px; font-size: 24px; line-height: 33px; }
  .services-lead { position: absolute; left: 9px; top: 323px; font-size: 24px; white-space: nowrap; }

  .service-list {
    position: absolute; left: 72px; top: 374px; width: 267px; height: 217px;
    border: 2px solid var(--hot-pink); border-radius: 11px;
    list-style: none; padding: 9px 0 0 9px; font-size: 24px; line-height: 33px;
  }

  .full-list { position: absolute; left: 9px; top: 616px; font-size: 24px; line-height: 33px; white-space: nowrap; }

  .feature-panel {
    position: absolute; left: 425px; top: 0; width: 775px; height: 686px;
    background: linear-gradient(to bottom, var(--rose-top), var(--rose-bottom));
    color: var(--white);
  }
  .feature-art {
    position: absolute; left: 180px; top: 0; width: 560px; height: 650px;
    background: linear-gradient(to bottom, var(--feature-tint-top), var(--feature-tint-bottom));
    opacity: 0.35;
  }
  .feature-word {
    position: absolute; left: -54px; top: 278px; width: 440px; height: 110px;
    transform: rotate(-90deg); text-align: center; font-size: 100px; line-height: 110px;
  }
  .feature-divider { position: absolute; left: 257px; top: 117px; width: 2px; height: 423px; background: rgba(255,255,255,0.9); }
  .qualities { position: absolute; left: 289px; top: 120px; list-style: none; font-size: 78px; line-height: 100px; }
  .email-line { position: absolute; left: 15px; top: 596px; font-size: 28px; white-space: nowrap; }
  .call-line { position: absolute; left: 15px; top: 636px; font-size: 36px; white-space: nowrap; }
</style>
</head>
<body>
<main class="card">
  <section class="info-panel">
    <h1 class="brand-name">Velvet Aisle &amp; Function</h1>
    <div class="brand-sub">Rentals</div>
    <div class="brand-rule"></div>

    <h2 class="about-title">About Us</h2>
    <p class="about-text">Whether you have become engaged or are celebrating a special occasion or event, Congratulations!</p>
    <p class="services-lead">Here are some of the services we offer</p>
    <ul class="service-list">
      <li>Weddings</li>
      <li>Engagements</li>
      <li>Anniversaries</li>
      <li>Birthdays</li>
      <li>School Formals</li>
      <li>Corporate Functions</li>
    </ul>
    <p class="full-list">To view the full list go to:<br>www.velvetaisleandfunctions.com</p>
  </section>

  <section class="feature-panel">
    <div class="feature-art" role="img" aria-label="Soft decorative wedding illustration area"></div>
    <div class="feature-word">weddings</div>
    <div class="feature-divider"></div>
    <ul class="qualities">
      <li>elegant</li>
      <li>professional</li>
      <li>personal</li>
      <li>perfect</li>
    </ul>
    <p class="email-line">vaafr@quokkamail.com</p>
    <p class="call-line">For more info call 0413 586 190</p>
  </section>
</main>
</body>
</html>
```